International Software Company Requires 3 Product Brochures.

Having just redesigned our website we require 3 brochures. 1 for each of our software products.
Our customers are global, blue chip, organisations and a professional, corporate style is required for each of the product brochures.
While each of the products are separate it should be clear that they are part of a family of products. All products are firmly marketed to the international oil and gas sector.
Rather than produce designs for 3 brochures straight away, we ask that designers produce a layout with a “unified theme” but with slight modifications adapted for each product. Please show the internal layout as well as the external cover.
Once we have chosen a design we will ask the designer to produce the three variations.
Designs should complement our new website design (not yet published) which can be found in the attachments section of this project.
The 3 products are…
VQT - time & cost estimation software
VQT is used by engineers to estimate the time and cost required to drill an oil or gas well. This involves modelling all the stages of drilling and then associating costs and risks to each stage before simulating the project using the Monte Carlo methodology to create a probabilistic result. The message is about delivering accurate and consistent results that communicate the project and risk to management. Attachment HLVQT1.jpg is a graphic we have previously used to illustrate the VQT process but we do not think is very effective.
PLW - materials & cost control software
PLW is used by drilling and logistics staff to keep very accurate and up-to-date track of all the costs and equipment associated with drilling a well. PLW quickly and accurately produces various cost and materials reports in what is a very complex and costly engineering project and where different departments (such as engineering or finance) have different needs. Attachment HLPLW1.jpg is a graphic we have previously used to illustrate the PLW process but we do not think is very effective.
ZNF – lessons learned software
ZNF is a web based system used by oil and gas companies to record and share lessons learned associated with drilling and maintaining wells. These are complex, expensive and often dangerous processes where it is vital that knowledge is shared between staff not matter where in the word they are located.
The brochure format we are looking for is double A4 bi-fold, (a front cover, 2 internal pages and a back page, A4 size.)
The brochures will be both printed and send out as PDFs to prospective clients.
Updates
Project Deadline Extended
Reason: We realise that our brief may not have been as clear as it could and a 3 brochure requirement may seem overwhelming.
We are updating the brief to ask designers to produce a layout with a “unified theme” but with slight modifications adapted for each product.
Initially we ask that designers give us an example of external and internal pages for a single product brochure as an example of the unified theme.
We are extending the deadline to allow for more entries.
We have just realised that the currency for this project was in USD and not GBP as we assumed. We have therefore substantially increased the
budget on this project, with a first place of $600-USD.
Engineers and financial staff within International oil and gas companies, i.e. GQ, Vardo, Torlakin etc.
Oil And Gas

```html
<!DOCTYPE html>
<html lang="en">
<head>
<meta charset="utf-8">
<title>Coreline Systems – VQT Brochure</title>
<link href="https://fonts.googleapis.com/css2?family=Oswald:wght@500&family=PT+Sans:wght@400;700&display=swap" rel="stylesheet">
<style>
:root{
  --teal-dark:#2f6470;
  --teal:#3f7a85;
  --teal-light:#5f959e;
  --grey-bg:#ececec;
  --ink:#2b2b2b;
  --paper:#ffffff;
  --box-top:#f4f4f4;
  --box-bot:#cfcfcf;
}
*{margin:0;padding:0;box-sizing:border-box}
html,body{width:1200px;height:999px;overflow:hidden}
body{background:var(--grey-bg);font-family:"PT Sans",Arial,sans-serif;color:var(--ink);position:relative}

/* ---------- cover spread ---------- */
.cover-spread{position:absolute;left:40px;top:40px;width:640px;height:440px;display:flex;box-shadow:0 4px 14px rgba(0,0,0,.25)}
.back-page{width:320px;height:100%;background:linear-gradient(180deg,var(--teal-light) 0%,var(--teal) 45%,var(--teal-dark) 100%);position:relative;color:#fff}
.address{position:absolute;bottom:34px;font-size:7px;line-height:1.35}
.address h3{font-size:10px;margin-bottom:10px}
.address h4{font-size:8px;font-weight:700;text-transform:uppercase}
.address--europe{left:24px}
.address--na{left:190px;bottom:80px}
.front-page{width:320px;height:100%;background:var(--paper);position:relative;overflow:hidden}
.brand{position:absolute;left:54px;top:34px;display:flex;align-items:center;gap:10px}
.brand-dot{width:22px;height:22px;border-radius:50%;background:var(--teal)}
.brand-name{font-size:17px;font-weight:700;color:var(--teal-dark);letter-spacing:1px}
.front-rule{position:absolute;left:0;right:0;top:88px;height:3px;background:var(--teal)}
.cover-photo{position:absolute;left:66px;top:118px;width:200px;height:150px;background:linear-gradient(180deg,#e9edf2,#b9c4d1)}
.cover-wave{position:absolute;left:0;bottom:0;width:320px;height:200px}
.web{position:absolute;left:0;right:0;bottom:30px;text-align:center;color:#fff;font-size:9px;letter-spacing:4px}

/* ---------- inside spread ---------- */
.inside-spread{position:absolute;left:522px;top:515px;width:651px;height:440px;display:flex;box-shadow:0 4px 14px rgba(0,0,0,.25)}
.inside-left{width:313px;height:100%;background:var(--paper);position:relative;border-right:1px solid #bbb}
.title-bar{height:36px;background:linear-gradient(90deg,var(--teal-dark) 88%,var(--teal-light) 88%);display:flex;align-items:center;padding-left:10px}
.title-bar h1{font-family:"Oswald",Impact,sans-serif;font-weight:500;color:#fff;font-size:19px;letter-spacing:.3px}
.intro{padding:14px 12px 0;font-size:8.6px;line-height:1.3;text-align:justify}
.intro p{margin-bottom:9px}
.key-points{position:absolute;left:0;right:0;top:218px;height:117px;background:linear-gradient(180deg,var(--teal-dark),var(--teal-light) 60%,#dfe8ea);padding:10px 12px 0 34px;color:#fff;font-size:8.6px;line-height:1.3}
.key-points li{margin-bottom:8px;text-align:justify}
.key-points b{font-weight:700}
.summary{position:absolute;left:12px;right:12px;top:350px;font-size:8.6px;line-height:1.3;text-align:justify}
.foot-band{position:absolute;left:0;right:0;bottom:0;height:10px;background:linear-gradient(180deg,var(--teal-light),var(--teal-dark))}
.head-band{position:absolute;left:0;right:0;top:0;height:8px;background:linear-gradient(180deg,var(--teal-light),var(--teal-dark))}
.inside-right{width:338px;height:100%;background:linear-gradient(90deg,#d9d9d9,#fff 40%,#fff 60%,#d9d9d9);position:relative}
.process{position:absolute;left:0;top:0}
.process text{font-family:"PT Sans",Arial,sans-serif;font-size:7.4px;fill:#222;text-anchor:middle}
</style>
</head>
<body>

<section class="cover-spread">
  <div class="back-page">
    <div class="address address--europe">
      <h3>Address</h3>
      <h4>Europe</h4>
      <p>18 Harbour Row<br>Aberdeen<br>AB11 4QT<br>Phone: +44(0)1224 550190<br>Email: eu@corelinesys.com</p>
    </div>
    <div class="address address--na">
      <h4>North America</h4>
      <p>4100 Westpark Dr<br>Suite 210<br>Houston, TX 77057<br>Phone: (713)555 0148<br>Email: us@corelinesys.com</p>
    </div>
  </div>
  <div class="front-page">
    <div class="brand"><span class="brand-dot"></span><span class="brand-name">CORELINE SYSTEMS</span></div>
    <div class="front-rule"></div>
    <div class="cover-photo" role="img" aria-label="Photo of an engineer working at a laptop"></div>
    <svg class="cover-wave" viewBox="0 0 320 200" aria-hidden="true">
      <defs>
        <linearGradient id="greyCurve" x1="0" y1="0" x2="0" y2="1"><stop offset="0" stop-color="#9a9a9a"/><stop offset="1" stop-color="#3e3e3e"/></linearGradient>
        <linearGradient id="tealWave" x1="0" y1="0" x2="0" y2="1"><stop offset="0" stop-color="#5f959e"/><stop offset="1" stop-color="#2f6470"/></linearGradient>
      </defs>
      <path d="M40 40 Q180 10 320 30 L320 80 Q180 60 40 70 Z" fill="url(#greyCurve)"/>
      <path d="M0 70 Q80 70 150 95 Q240 120 320 60 L320 200 L0 200 Z" fill="url(#tealWave)"/>
    </svg>
    <p class="web">www.corelinesys.com</p>
  </div>
</section>

<section class="inside-spread">
  <div class="inside-left">
    <div class="title-bar"><h1>THE BUSINESS OF DRILLING WELLS</h1></div>
    <div class="intro">
      <p>VQT allows engineers to combine their experience and fundamental principles with offset and historical data to produce enhanced, probabilistic time and costs forecasts that are consistent across operations.</p>
      <p>Probabilistic AFEs produced with VQT allow operators to take a more analytical approach, giving them the ability to quickly evaluate different prospects before committing financial resources for drilling projects.</p>
      <p>VQT is template driven so you can build a model for any type of activity. For drilling teams this means the product is appropriate whether it be early appraisal work or a detailed AFE, a single exploration well or a fifty well development campaign.</p>
    </div>
    <ul class="key-points">
      <li><b>VQT</b> allows organizations to be consistent in the way time and cost estimates are generated</li>
      <li><b>VQT</b> can accommodate any type of project from high level appraisal work to detailed planning to the last line item</li>
      <li><b>VQT</b> facilitates clear communication of risk and cost to decision-makers and other stakeholders</li>
    </ul>
    <p class="summary">VQT v5.0 launches improved multi-well AFE generation and offset-data mapping. Using VQT provides an efficient and common process for AFE generation that reduces errors, increases user productivity and speeds up the decision making process.</p>
    <div class="foot-band"></div>
  </div>

  <div class="inside-right">
    <div class="head-band"></div>
    <svg class="process" width="338" height="440" viewBox="0 0 338 440">
      <defs>
        <linearGradient id="box" x1="0" y1="0" x2="0" y2="1"><stop offset="0" stop-color="#f6f6f6"/><stop offset="1" stop-color="#c9c9c9"/></linearGradient>
        <linearGradient id="funnel" x1="0" y1="0" x2="0" y2="1"><stop offset="0" stop-color="#d6d6d6"/><stop offset="1" stop-color="#9c9c9c"/></linearGradient>
        <radialGradient id="ball" cx=".4" cy=".35" r=".7"><stop offset="0" stop-color="#fafafa"/><stop offset="1" stop-color="#bdbdbd"/></radialGradient>
        <marker id="tip" viewBox="0 0 10 10" refX="5" refY="5" markerWidth="5" markerHeight="5" orient="auto"><path d="M0 0 L10 5 L0 10 Z" fill="#111"/></marker>
      </defs>
      <g stroke="#777" stroke-width=".8">
        <path d="M62 28 L242 28 L182 108 L124 108 Z" fill="url(#funnel)"/>
        <g fill="#f3f3f3">
          <rect x="102" y="36" width="62" height="18" transform="rotate(-10 133 45)"/>
          <rect x="146" y="47" width="62" height="18" transform="rotate(-16 177 56)"/>
          <rect x="116" y="66" width="62" height="18" transform="rotate(8 147 75)"/>
        </g>
        <g fill="url(#box)">
          <rect x="95" y="110" width="115" height="25"/>
          <rect x="33" y="148" width="117" height="25"/>
          <rect x="152" y="148" width="116" height="25"/>
          <rect x="33" y="183" width="117" height="25"/>
          <rect x="152" y="183" width="116" height="25"/>
          <circle cx="150" cy="257" r="42" fill="url(#ball)"/>
          <path d="M93 318 L208 318 L208 338 L150 348 L93 338 Z"/>
          <path d="M93 352 L208 352 L208 372 L150 380 L93 372 Z"/>
          <rect x="93" y="390" width="115" height="23"/>
        </g>
      </g>
      <text x="133" y="47" transform="rotate(-10 133 45)">Spreadsheets</text>
      <text x="177" y="58" transform="rotate(-16 177 56)">Documents</text>
      <text x="147" y="78" transform="rotate(8 147 75)">Processes</text>
      <text x="152" y="121">Templates created from</text>
      <text x="152" y="130">Existing Processes</text>
      <text x="91" y="159">Create Project Structure</text>
      <text x="91" y="168">and associate costs</text>
      <text x="210" y="159">Multiply and edit</text>
      <text x="210" y="168">Single Well models</text>
      <text x="91" y="194">Include options for</text>
      <text x="91" y="203">comparison / model NPT</text>
      <text x="210" y="194">Learning &amp; NPT curves,</text>
      <text x="210" y="203">re-order &amp; run scenarios</text>
      <text x="150" y="242">VQT</text>
      <text x="150" y="252">Monte</text>
      <text x="150" y="262">Carlo</text>
      <text x="150" y="272">Simulation</text>
      <text x="150" y="334">Generate Results</text>
      <text x="150" y="367">Analyse &amp; Understand</text>
      <text x="150" y="404">Reports</text>
      <g fill="none" stroke="#111" stroke-width="3.5" marker-end="url(#tip)">
        <path d="M70 214 Q72 232 96 244"/>
        <path d="M232 214 Q230 232 206 244"/>
        <path d="M150 302 L150 310" stroke-width="2.5"/>
      </g>
    </svg>
    <div class="foot-band"></div>
  </div>
</section>

</body>
</html>
```